7 3/4 x 5 1/4 Annual Banquet Invitation

Design an invitation for our Chamber's annual banquet. It will be a single sided invitation 5 1/4" wide by 7 3/4" height that we will print in-house. Our logo is attached. The theme is "Serving Together". I was thinking of an image with two hands coming together in a handshake, perhaps intertwining our logo colors. This is just a thought. I am open for any suggestions! Text for the invitation should be as follows: The Board of Directors and Staff cordially invites you to attend the 64th Yearly Gathering & Micro-Trade Fair - Monday, January 22, 2018. 5:30 p.m. Social, 6:00 p.m. Dinner. Cedarvale Chapel, 4819 Harlan P. Moss Rd S, Larkmoor. Please RSVP by January 18, 2018.

Target Market(s)

This invitation will be printed and mailed to our membership.

Industry/Entity Type

Business Management

Colors
33a6d7
faa54b
0355a3
00a990

Requirements
Must have
• Event info as indentified above.
Nice to have
• Our Logo

```html
<!DOCTYPE html>
<html lang="en">
<head>
<meta charset="utf-8">
<title>64th Yearly Gathering &amp; Micro-Trade Fair – Invitation</title>
<link rel="stylesheet" href="https://fonts.googleapis.com/css2?family=Roboto:wght@300;400;500;700&display=swap">
<style>
  :root {
    --ink-blue: #1f4e9a;
    --navy: #0355a3;
    --sky: #33a6d7;
    --teal: #00a990;
    --orange: #faa54b;
    --red: #e21f26;
    --paper: #f1f1f2;
    --paper-light: #fbfbfb;
    --grey: #9a9b9d;
    --label: #333;
  }
  * { box-sizing: border-box; margin: 0; padding: 0; }
  html, body { width: 864px; height: 1200px; overflow: hidden; background: #fff; }
  body { font-family: "Roboto", sans-serif; }

  .invitation {
    position: relative;
    width: 864px;
    height: 1200px;
    overflow: hidden;
    background: radial-gradient(ellipse at 50% 40%, var(--paper-light) 0%, var(--paper) 60%, #e4e4e5 100%);
  }

  .hero-photo {
    position: absolute;
    left: 0; top: 0;
    width: 864px; height: 560px;
    background:
      radial-gradient(ellipse at 50% 30%, rgba(255,255,255,.9) 0%, rgba(255,255,255,0) 60%),
      linear-gradient(180deg, #ececed 0%, #e0e1e2 70%, rgba(241,241,242,0) 100%);
  }
  .hero-hands {
    position: absolute;
    left: 0; top: 128px;
    width: 864px; height: 296px;
    background: linear-gradient(100deg, #3c4654 0%, #56606c 30%, #9c7561 45%, #6a4a3a 55%, #8e9297 70%, #a7aaad 100%);
    opacity: .85;
    border-radius: 0 0 40% 40% / 0 0 30% 30%;
  }

  .hosts {
    position: absolute;
    top: 30px; left: 0; width: 100%;
    text-align: center;
    color: var(--ink-blue);
    z-index: 2;
  }
  .hosts__line1 { font-weight: 300; font-size: 36px; line-height: 44px; }
  .hosts__line2 { font-size: 48px; line-height: 54px; font-weight: 300; }
  .hosts__line2 strong { color: var(--red); font-weight: 700; }

  .invite-arc { position: absolute; left: 0; top: 430px; width: 864px; height: 140px; }
  .invite-arc text { font-family: "Roboto", sans-serif; font-size: 31px; fill: var(--ink-blue); }

  .ribbon {
    position: absolute;
    left: 0; top: 601px;
    width: 864px; height: 55px;
    background: var(--orange);
  }

  .badge {
    position: absolute;
    left: 333px; top: 532px;
    width: 196px; height: 196px;
    border-radius: 50%;
    background: var(--orange);
    padding: 9px;
  }
  .badge__inner {
    width: 178px; height: 178px;
    border-radius: 50%;
    background: var(--ink-blue);
    color: #fff;
    text-align: center;
    font-size: 82px; font-weight: 400;
    line-height: 178px;
    letter-spacing: -2px;
  }
  .badge__ordinal {
    position: relative;
    top: -34px;
    margin-left: 4px;
    font-size: 30px;
    letter-spacing: 0;
  }

  .event-title {
    position: absolute;
    top: 754px; left: 0; width: 100%;
    text-align: center;
  }
  .event-title__line1 { font-size: 38px; line-height: 42px; color: var(--ink-blue); font-weight: 300; }
  .event-title__line2 { font-size: 38px; line-height: 42px; color: var(--teal); font-weight: 300; }

  .fair-tiles {
    position: absolute;
    top: 847px; left: 282px;
    display: flex; gap: 6px;
  }
  .fair-tiles span {
    width: 67px; height: 54px;
    display: flex; align-items: center; justify-content: center;
    font-size: 46px; font-weight: 500; color: #fff;
  }
  .tile--navy { background: var(--ink-blue); }
  .tile--teal { background: var(--teal); color: var(--red) !important; }
  .tile--sky { background: var(--sky); color: var(--ink-blue) !important; }
  .tile--orange { background: var(--orange); }

  .icon-network {
    position: absolute;
    left: 67px; top: 771px;
    width: 130px; height: 124px;
    border-radius: 50%;
    background: radial-gradient(circle, #9fb6d6 0%, #d7e1ee 55%, rgba(241,241,242,0) 72%);
  }
  .sketch-meeting {
    position: absolute;
    left: 598px; top: 784px;
    width: 242px; height: 121px;
    background: linear-gradient(180deg, #e9ecf3 0%, #d9dfeb 100%);
    border-radius: 6px;
  }

  .details {
    position: absolute;
    top: 939px; left: 0; width: 864px; height: 70px;
  }
  .details__col {
    position: absolute; top: 0;
    text-align: center;
    transform: translateX(-50%);
    white-space: nowrap;
  }
  .details__col--date { left: 131px; }
  .details__col--time { left: 368px; }
  .details__col--place { left: 670px; }
  .details__label { font-size: 15px; color: var(--label); line-height: 22px; margin-top: 2px; }
  .details__value { font-size: 19px; color: var(--ink-blue); line-height: 26px; }
  .details__divider {
    position: absolute; top: 0;
    width: 1px; height: 68px;
    background: var(--teal);
  }
  .details__divider--a { left: 253px; }
  .details__divider--b { left: 491px; }

  .chamber-mark {
    position: absolute;
    left: 597px; top: 1082px;
    width: 236px;
    text-align: center;
    color: var(--ink-blue);
    font-weight: 700;
  }
  .chamber-mark__dot {
    width: 46px; height: 46px;
    border-radius: 50%;
    background: var(--sky);
    margin: 0 auto 12px;
  }
  .chamber-mark__name { font-size: 20px; line-height: 22px; }
  .chamber-mark__sub { font-size: 11px; letter-spacing: 3.2px; line-height: 14px; }

  .footer-bar { position: absolute; left: 0; top: 1176px; width: 864px; height: 24px; }
</style>
</head>
<body>
<main class="invitation">
  <div class="hero-photo" role="img" aria-label="Faint grey world map background"></div>
  <div class="hero-hands" role="img" aria-label="Photograph of two businessmen in suits shaking hands"></div>

  <header class="hosts">
    <p class="hosts__line1">The Board of</p>
    <p class="hosts__line2"><strong>Directors</strong> and <strong>Staff</strong></p>
  </header>

  <svg class="invite-arc" viewBox="0 430 864 140" aria-label="cordially invites you to attend the">
    <defs>
      <path id="arc-upper" d="M280 528 Q432 420 588 526"/>
      <path id="arc-lower" d="M325 548 Q432 468 534 548"/>
    </defs>
    <text><textPath href="#arc-upper" startOffset="50%" text-anchor="middle">cordially invites you</textPath></text>
    <text><textPath href="#arc-lower" startOffset="50%" text-anchor="middle">to attend the</textPath></text>
  </svg>

  <div class="ribbon"></div>
  <div class="badge"><div class="badge__inner">64<span class="badge__ordinal">th</span></div></div>

  <div class="icon-network" role="img" aria-label="Icon of a globe with two business people connected by a circular arrow"></div>

  <section class="event-title">
    <h1 class="event-title__line1">Yearly Gathering</h1>
    <h2 class="event-title__line2">&amp; Micro-Trade</h2>
  </section>
  <div class="fair-tiles" aria-label="Fair">
    <span class="tile--navy">F</span>
    <span class="tile--teal">A</span>
    <span class="tile--sky">I</span>
    <span class="tile--orange">R</span>
  </div>

  <div class="sketch-meeting" role="img" aria-label="Line sketch of business people meeting around a table"></div>

  <section class="details">
    <div class="details__col details__col--date">
      <p class="details__label">Date :</p>
      <p class="details__value">Monday<br>January 22, 2018</p>
    </div>
    <div class="details__divider details__divider--a"></div>
    <div class="details__col details__col--time">
      <p class="details__label">Time :</p>
      <p class="details__value">5:30 p.m. Social<br>6:00 p.m. Dinner</p>
    </div>
    <div class="details__divider details__divider--b"></div>
    <div class="details__col details__col--place">
      <p class="details__label">Place :</p>
      <p class="details__value">Cedarvale Chapel, 4819 Harlan<br>P. Moss Rd S, Larkmoor.</p>
    </div>
  </section>

  <div class="chamber-mark">
    <div class="chamber-mark__dot"></div>
    <p class="chamber-mark__name">RIDGEFORD CHAMBER</p>
    <p class="chamber-mark__sub">OF COMMERCE &amp; TOURISM</p>
  </div>

  <svg class="footer-bar" viewBox="0 0 864 24" preserveAspectRatio="none">
    <polygon points="550,8 864,8 864,24 566,24" fill="var(--grey)"/>
    <polygon points="0,0 552,0 568,24 0,24" fill="var(--sky)"/>
  </svg>
</main>
</body>
</html>
```